Seafood company needs a label design

Our brand name is Coral Tide Fisheries. We need a label design for a new product line of 200g trays of sardine fillets. The label/sleeve is going to wrap around the black tray. We are a family owned and operated business in Esperance, Western Australia. We would like simple appealing designs that catch the eye of the consumer.

Target Market(s)

seafood consumers in supermarkets

Colors

Designer to choose colors to be used in the design.

Requirements
Must have
• The front of the label must include
• •Coral Tide Fisheries
• •since 1997
• •Sustainably wild caught from the pristine southern ocean Esperance Western Australia
Nice to have
• Deep/Rich colours, and black, maybe Drawn picture of sardine/sardines or an anchor fast anchor.
Should not have
• cartoon images, not too cluttered

```html
<!DOCTYPE html>
<html lang="en">
<head>
<meta charset="utf-8">
<title>Coral Tide Fisheries – Sardine Fillets Label</title>
<link rel="stylesheet" href="https://fonts.googleapis.com/css2?family=Oswald:wght@300;400&family=Courier+Prime&display=swap">
<style>
  :root {
    --page: #ffffff;
    --ink: #2b2b2b;
    --frame: #2f2f2f;
    --label: #ffffff;
    --gold: #f2d21b;
    --photo-top: #e9d7c6;
    --photo-mid: #c9774a;
    --photo-low: #6f9a4a;
  }
  * { box-sizing: border-box; margin: 0; padding: 0; }
  html, body {
    width: 1200px; height: 1200px; overflow: hidden;
    background: var(--page);
  }
  .canvas { position: relative; width: 1200px; height: 1200px; }

  .label {
    position: absolute; left: 83px; top: 296px;
    width: 1037px; height: 605px;
    background: var(--label);
    border: 13px solid var(--frame);
    border-radius: 54px;
    box-shadow: 0 26px 30px -14px rgba(0,0,0,0.35);
  }

  /* brand block */
  .brand-name {
    position: absolute; left: 170px; top: 640px; width: 420px;
    text-align: center;
    font-family: "Oswald", sans-serif; font-weight: 400;
    font-size: 52px; line-height: 1.1; letter-spacing: 3px;
    color: var(--ink); text-transform: uppercase;
  }
  .pill {
    position: absolute; top: 516px; height: 55px;
    border: 5px solid var(--gold); border-radius: 28px;
    font-family: "Oswald", sans-serif; font-weight: 300;
    font-size: 36px; line-height: 45px; color: var(--ink);
    text-transform: uppercase;
  }
  .pill--since { left: 117px; width: 167px; padding-left: 20px; }
  .pill--year { left: 496px; width: 147px; text-align: right; padding-right: 22px; }
  .since-rule {
    position: absolute; left: 284px; top: 541px; width: 212px; height: 5px;
    background: var(--ink);
  }

  /* product panel */
  .product-frame { position: absolute; left: 688px; top: 322px; }
  .product-photo {
    position: absolute; left: 757px; top: 417px; width: 226px; height: 150px;
    background: linear-gradient(160deg, var(--photo-top) 0%, var(--photo-mid) 55%, var(--photo-low) 100%);
  }
  .product-weight, .product-name {
    position: absolute; left: 700px; width: 340px; text-align: center;
    font-family: "Oswald", sans-serif; font-weight: 400;
    font-size: 38px; line-height: 1; color: var(--gold);
    text-transform: uppercase;
  }
  .product-weight { top: 575px; }
  .product-name { top: 628px; }
  .product-origin {
    position: absolute; left: 716px; top: 672px; width: 308px;
    font-family: "Courier Prime", monospace; font-size: 17px; line-height: 24px;
    color: var(--ink); text-align: justify; text-align-last: left;
  }
</style>
</head>
<body>
<main class="canvas">
  <section class="label">
  </section>

  <div class="since-rule"></div>
  <div class="pill pill--since">Since</div>
  <div class="pill pill--year">1997</div>
  <h1 class="brand-name">Coral Tide<br>Fisheries</h1>

  <svg class="product-frame" width="362" height="536" viewBox="0 0 362 536" aria-hidden="true">
    <path d="M181 6 L350 92 Q356 95 356 102 L356 434 Q356 441 350 444 L181 530 L12 444 Q6 441 6 434 L6 102 Q6 95 12 92 Z"
          fill="none" stroke="var(--gold)" stroke-width="5" stroke-linejoin="round"/>
    <path d="M56 64 L181 20 L306 64" fill="none" stroke="var(--ink)" stroke-width="3"/>
    <path d="M56 472 L181 516 L306 472" fill="none" stroke="var(--ink)" stroke-width="3"/>
  </svg>
  <div class="product-photo" role="img" aria-label="Photo of sardine fillets served on a white plate with green salad and herb dip"></div>
  <p class="product-weight">200g</p>
  <p class="product-name">Sardine Fillets</p>
  <p class="product-origin">Sustainably wild caught from the pristine southern ocean Esperance Western Australia</p>
</main>
</body>
</html>
```